Labels design for moisturizer cream and Serum

We need our label to be design for our two skincare products - moisturizer & Serum.
The products are premium so they need to look clean and prestigious. Have it look similar to our logo (Attached for now with watermarks)

The 2 product names are:
Velvet Dawn Facial Serum
Amber Meadow Moisturizer

```html
<!DOCTYPE html>
<html lang="en">
<head>
<meta charset="utf-8">
<title>LUMERA Paris – Amber Meadow Moisturizer Labels</title>
<link rel="stylesheet" href="https://fonts.googleapis.com/css2?family=Arimo:wght@400;700&family=Roboto+Condensed:wght@400;700&display=swap">
<style>
  :root {
    --paper: #ffffff;
    --ink: #111111;
    --night: #050505;
    --dieline: #9a9a9a;
    --gold-light: #f3e3b4;
    --gold: #c9922f;
    --bronze: #7a4a1c;
    --cream: #f4f1ea;
    --silver: #b9bcc0;
  }
  * { box-sizing: border-box; margin: 0; padding: 0; }
  html, body { width: 1200px; height: 929px; overflow: hidden; background: var(--paper); }
  .sheet { position: relative; width: 1200px; height: 929px; font-family: "Arimo", Arial, sans-serif; color: var(--ink); }
  .shapes { position: absolute; inset: 0; }
  .panel { position: absolute; white-space: nowrap; font-family: "Roboto Condensed", "Arial Narrow", sans-serif; font-weight: 400; }
  .brand-block { position: absolute; left: 450px; width: 300px; text-align: center; }
  .brand-name { font-weight: 400; font-size: 42px; letter-spacing: 2px; line-height: 42px; }
  .brand-city { font-size: 7px; letter-spacing: 9px; margin-top: 2px; padding-left: 9px; }
  .product-name { font-size: 13px; margin-top: 6px; }
  .net { font-size: 10px; margin-top: 6px; }

  .label-light .ingredients { left: 62px; top: 78px; font-size: 9.2px; line-height: 13px; transform: rotate(-4.5deg); transform-origin: left top; }
  .label-light .directions { left: 850px; top: 68px; font-size: 10px; line-height: 13px; transform: rotate(4deg); transform-origin: left top; }
  .label-light .brand-block { top: 66px; }

  .label-dark { color: var(--paper); }
  .label-dark .panel { font-weight: 700; }
  .label-dark .ingredients { left: 54px; top: 472px; font-size: 8px; line-height: 10.4px; transform: rotate(-4deg); transform-origin: left top; }
  .label-dark .directions { left: 855px; top: 458px; font-size: 8.8px; line-height: 11.4px; transform: rotate(4deg); transform-origin: left top; }
  .label-dark .brand-block { top: 452px; }
  .label-dark .product-name { margin-top: 5px; }

  .jar { position: absolute; }
  .jar-light { background: linear-gradient(180deg, var(--silver) 0 22%, #f5f5f5 22%, #e6e6e6 100%); border-radius: 4px 4px 18px 18px; }
  .jar-dark { border-radius: 18px; }
</style>
</head>
<body>
<main class="sheet">
  <svg class="shapes" width="1200" height="929" viewBox="0 0 1200 929" aria-hidden="true">
    <defs>
      <linearGradient id="gold-band" x1="0" x2="1" y1="0" y2="0">
        <stop offset="0" stop-color="var(--cream)"/>
        <stop offset="0.18" stop-color="var(--gold-light)"/>
        <stop offset="0.3" stop-color="var(--gold)"/>
        <stop offset="0.5" stop-color="var(--gold-light)"/>
        <stop offset="0.62" stop-color="var(--bronze)"/>
        <stop offset="0.8" stop-color="var(--gold)"/>
        <stop offset="1" stop-color="var(--cream)"/>
      </linearGradient>
    </defs>
    <path d="M40 56 Q600 12 1152 53 L1146 196 Q600 150 46 202 Z" fill="none" stroke="var(--dieline)" stroke-dasharray="4 3"/>
    <path d="M50 66 Q600 24 1142 62 Q1144 62 1144 66 L1138 182 Q600 140 54 192 Z" fill="var(--paper)" stroke="var(--ink)" stroke-width="1.4" stroke-linejoin="round"/>
    <path d="M34 462 Q600 416 1142 460 L1136 592 Q600 548 40 598 Z" fill="none" stroke="var(--dieline)" stroke-dasharray="4 3"/>
    <path d="M42 470 Q600 426 1132 468 L1126 584 Q600 540 48 590 Z" fill="var(--night)"/>
    <path d="M47 566 Q600 516 1127 560 L1126 576 Q600 532 48 582 Z" fill="url(#gold-band)"/>
  </svg>

  <section class="label-light">
    <p class="panel ingredients">Ingredients: Purified Water, Acetyl Hexapeptide-38, Glycerin, Caprylic/Capric<br>Triglyceride, Persea Gratissima (Avocado) Oil, Butylene Glycol, Malus Domestica,<br>Paeonia Albiflora (Peony) Flower Extract, Chinesis (Jojoba) Seed Oil, Stearic Acid,<br>Cetyl Alcohol, Glyceryl Stearate, Peg 100 Stearate, Dimeticone, Aloe Barbedensis Extract,<br>Peg-16 Macademia Glycerides, Octyldocenol, Propylene Glycol, Zea Mays (Corn) Oil,<br>Tocopheryl Acetate, Cholecalciferol, Retinyl Palmitate, Ascorbic Acid, Pyridoxine HCl,<br>Silicate, Sodium Propoxyhydroxipropyl Thiosulfate, Silica, Polisorbate 20,<br>Phenocyethanol, Caprylyl Glycol, Potassium Sorbate, Hexylene Glycol</p>
    <div class="brand-block">
      <div class="brand-name">LUMERA</div>
      <div class="brand-city">PARIS</div>
      <div class="product-name">Amber Meadow Moisturizer</div>
      <div class="net">1oz/ 30ml</div>
    </div>
    <p class="panel directions">Directions: Apply a pea to dime size amount of cream to the face<br>and neck twice a day, or as needed. Smooth gently into skin after<br>cleansing and toning. Allow to absorb fully before applying<br>make-up.<br>Cautions: For external use only. Avoid direct contact with eyes and<br>mouth. If irritation occurs, discontinue use. KEEP OUT OF REACH<br>OF CHILDREN.</p>
  </section>

  <div class="jar jar-light" style="left:366px;top:228px;width:196px;height:158px;" role="img" aria-label="White jar with silver lid showing the ingredients side of the light label"></div>
  <div class="jar jar-light" style="left:595px;top:228px;width:188px;height:158px;" role="img" aria-label="White jar with silver lid showing the brand side of the light label"></div>

  <section class="label-dark">
    <p class="panel ingredients">Ingredients: Purified Water, Acetyl Hexapeptide-38, Glycerin, Caprylic/Capric<br>Triglyceride, Persea Gratissima (Avocado) Oil, Butylene Glycol, Malus Domestica,<br>Paeonia Albiflora (Peony) Flower Extract, Chinesis (Jojoba) Seed Oil, Stearic Acid,<br>Cetyl Alcohol, Glyceryl Stearate, Peg 100 Stearate, Dimeticone, Aloe Barbedensis Extract,<br>Peg-16 Macademia Glycerides, Octyldocenol, Propylene Glycol, Zea Mays (Corn) Oil,<br>Tocopheryl Acetate, Cholecalciferol, Retinyl Palmitate, Ascorbic Acid, Pyridoxine HCl,<br>Silicate, Sodium Propoxyhydroxipropyl Thiosulfate, Silica, Polisorbate 20,<br>Phenocyethanol, Caprylyl Glycol, Potassium Sorbate, Hexylene Glycol</p>
    <div class="brand-block">
      <div class="brand-name">LUMERA</div>
      <div class="brand-city">PARIS</div>
      <div class="product-name">Amber Meadow Moisturizer</div>
      <div class="net">1oz/ 30ml</div>
    </div>
    <p class="panel directions">Directions: Apply a pea to dime size amount of cream to the face and<br>neck twice a day, or as needed. Smooth gently into skin after cleansing<br>and toning. Allow to absorb fully before applying make-up.<br>Cautions: For external use only. Avoid direct contact with eyes and<br>mouth. If irritation occurs, discontinue use. KEEP OUT OF REACH OF<br>CHILDREN.</p>
  </section>

  <div class="jar jar-dark" style="left:370px;top:635px;width:196px;height:172px;background:linear-gradient(180deg,var(--gold-light) 0 22%,var(--night) 22%,#2a1a0c 60%,var(--night) 100%);" role="img" aria-label="Dark jar with gold lid showing the ingredients side of the dark label"></div>
  <div class="jar jar-dark" style="left:600px;top:635px;width:196px;height:172px;background:linear-gradient(180deg,var(--gold-light) 0 22%,var(--night) 22%,#1c1c1c 60%,var(--night) 100%);" role="img" aria-label="Dark jar with gold lid showing the brand side of the dark label"></div>
</main>
</body>
</html>
```